Tessellaria

Club flyer, grand opening night, house/electronic music, looking for clean design with a sample image attached. Please look at the prior flyers to get an idea of the style. Guaranteed project
I would like to use the red design if possible (tessellaria flyer attached)
Text:
TESSELLARIA
Winter House Music Monthly
Opening Night Dec 13 2013
Pellmont (use logo)
Featuring
BRAMOX (House/Garage)
(use logo with just Bramox name)
w/ resident
ORV (Driftwerk)
Free All Night
21-39 year old club with all house/electronic music. classier and grown up over gimmicky
Club

```html
<!DOCTYPE html>
<html lang="en">
<head>
<meta charset="utf-8">
<title>Tessellaria – Opening Night</title>
<link rel="stylesheet" href="https://fonts.googleapis.com/css2?family=Archivo+Black&family=Open+Sans:ital,wght@0,400;0,700;0,800;1,400&display=swap">
<style>
  :root {
    --band-dark: #1c2129;
    --band-stripe: #2a303a;
    --stage-light: #f6f6f7;
    --stage-mid: #cdced1;
    --floor: #ffffff;
    --footer-top: #f3f3f3;
    --footer-bottom: #d0d0d2;
    --ink: #1f1f1f;
    --navy: #1d3b8f;
    --white: #ffffff;
    --tone-orange: rgba(232, 78, 22, 0.55);
    --tone-green: rgba(140, 196, 30, 0.5);
    --tone-purple: rgba(120, 20, 100, 0.45);
    --tone-blue: rgba(20, 90, 190, 0.45);
    --tone-yellow: rgba(245, 180, 20, 0.45);
  }
  * { margin: 0; padding: 0; box-sizing: border-box; }
  html, body { width: 848px; height: 1200px; overflow: hidden; background: #fff; }
  .flyer { position: relative; width: 848px; height: 1200px; overflow: hidden; font-family: "Open Sans", Arial, sans-serif; }
  .striped { background: repeating-linear-gradient(90deg, var(--band-dark) 0 18px, var(--band-stripe) 18px 36px); }

  .header-band { position: absolute; left: 0; top: 0; width: 848px; height: 170px; box-shadow: inset 0 -30px 40px rgba(0,0,0,0.25); }
  .opening-label {
    position: absolute; left: 70px; top: 142px;
    transform: rotate(-90deg); transform-origin: left top;
    color: var(--white); font-family: "Archivo Black", sans-serif;
    font-size: 16px; line-height: 18px; letter-spacing: 0.5px;
  }
  .event-date { position: absolute; left: 124px; top: 30px; color: var(--white); font-family: "Archivo Black", sans-serif; }
  .event-date .day { display: block; font-size: 54px; line-height: 50px; letter-spacing: -1px; }
  .event-date .year { display: block; font-size: 74px; line-height: 66px; letter-spacing: -2px; }
  .free-badge { position: absolute; left: 632px; top: 8px; width: 152px; height: 152px; }

  .stage {
    position: absolute; left: 0; top: 170px; width: 848px; height: 646px;
    background: radial-gradient(ellipse at 55% 45%, var(--stage-light) 0%, #e6e6e8 55%, var(--stage-mid) 100%);
  }
  .stage-artwork {
    position: absolute; left: 104px; top: 114px; width: 668px; height: 532px;
    background:
      radial-gradient(circle at 50% 78%, var(--tone-orange) 0 14%, transparent 40%),
      radial-gradient(circle at 66% 50%, var(--tone-green) 0 10%, transparent 34%),
      radial-gradient(circle at 38% 72%, var(--tone-purple) 0 8%, transparent 30%),
      radial-gradient(circle at 76% 80%, var(--tone-blue) 0 6%, transparent 26%),
      radial-gradient(circle at 28% 92%, var(--tone-yellow) 0 8%, transparent 26%);
  }
  .floor { position: absolute; left: 0; top: 816px; width: 848px; height: 64px; background: linear-gradient(var(--floor), #f3f3f3); }

  .title-band { position: absolute; left: 0; top: 880px; width: 848px; height: 174px; }
  .title {
    position: absolute; left: 0; width: 848px; top: 20px; text-align: center;
    font-weight: 800; font-size: 84px; line-height: 96px; letter-spacing: 1px;
    background: linear-gradient(#ffffff 0%, #e4e4e4 50%, #9a9a9a 100%);
    -webkit-background-clip: text; background-clip: text; color: transparent;
  }
  .subtitle { position: absolute; left: 0; width: 848px; top: 108px; text-align: center; color: var(--white); font-size: 34px; line-height: 40px; }

  .footer { position: absolute; left: 0; top: 1054px; width: 848px; height: 146px; background: linear-gradient(var(--footer-top), var(--footer-bottom)); }
  .featuring { position: absolute; left: 68px; top: 14px; font-size: 23px; line-height: 30px; color: var(--ink); }
  .headliner { position: absolute; left: 68px; top: 50px; font-family: "Archivo Black", sans-serif; font-size: 54px; line-height: 60px; color: var(--navy); }
  .genres { position: absolute; left: 116px; top: 108px; font-size: 14px; font-weight: 700; color: var(--navy); }
  .resident { position: absolute; right: 68px; top: 52px; text-align: right; }
  .resident-label { font-size: 23px; color: var(--ink); line-height: 30px; }
  .resident-name { font-size: 23px; color: var(--navy); line-height: 30px; font-weight: 700; }
  .resident-name em { font-weight: 400; }
</style>
</head>
<body>
<div class="flyer">
  <header class="header-band striped">
    <div class="opening-label">OPENING<br>NIGHT</div>
    <div class="event-date"><span class="day">DEC13</span><span class="year">2013</span></div>
    <svg class="free-badge" viewBox="0 0 152 152" aria-label="Free all night">
      <polygon fill="#ffffff" points="76,2 88,44 126,16 110,58 150,62 112,82 140,118 98,106 92,150 74,112 50,146 52,104 10,118 40,84 2,62 44,56 22,18 62,42"/>
      <g transform="rotate(-22 76 76)" font-family="Open Sans, sans-serif" font-style="italic" font-weight="800" fill="#1f1f1f" text-anchor="middle">
        <text x="78" y="78" font-size="22">FREE</text>
        <text x="80" y="94" font-size="13">All Night</text>
      </g>
    </svg>
  </header>

  <section class="stage">
    <div class="stage-artwork" role="img" aria-label="Illustration of colourful speaker towers with round speakers on curving cables"></div>
  </section>
  <div class="floor"></div>

  <section class="title-band striped">
    <h1 class="title">TESSELLARIA</h1>
    <p class="subtitle">WINTER HOUSE MUSIC MONTHLY</p>
  </section>

  <footer class="footer">
    <div class="featuring">Featuring</div>
    <div class="headliner">BRAMOX</div>
    <div class="genres">house · garage · 2step</div>
    <div class="resident">
      <div class="resident-label">w/ resident</div>
      <div class="resident-name">ORV <em>(Driftwerk)</em></div>
    </div>
  </footer>
</div>
</body>
</html>
```